Tavio's Wine Label Design

Design for a wine bottle label. It'Is for A Dog Bar. This bar is upscale, so I am going for an elegant look
Here is what I am requesting.
1.Label to fit a wine bottle 4" Wide x 5" Length
1. Black Matte or Slate if you if you are having trouble with colors
2. The writing done in Gold Foil
3. Please consider the what the logo looks like- also it has a copy write on the art. If you can insert that it would be nicel
4. Please have print the says the "Pup Baron's Pick"
5. Please Incorporate Sandmere Beach Florida
www.tavioberlanzi.example and 555-304-8812
5. Product de France
4. Please incorporate the photo of the dog attached
6. I have added a couple of example label photos to give you an idea of the feel of the look I am seeking
7.One Type of wine is Chardonnay
8.One type of wine is Pinot Noir
8. Notice the image with the dog paw incorporate in the scroll work. Love that!

Target Market(s)

Dog and Upscale Wine lovers

Font styles to use
Decorative
Script

Requirements
Must have
• See Project Description
Nice to have
• Copy right symbol after logo

```html
<!DOCTYPE html>
<html lang="en">
<head>
<meta charset="utf-8">
<title>Tavio Berlanzi – Pinot Noir Label</title>
<link rel="stylesheet" href="https://fonts.googleapis.com/css2?family=Cinzel:wght@400;500&family=Tinos&display=swap">
<style>
  :root {
    --backdrop: #d9d9d9;
    --label-black: #1c1b1a;
    --label-edge: #121111;
    --gold: #c9b07a;
    --gold-deep: #9c8352;
    --gold-band: #b79e69;
    --ivory: #f1ece2;
    --photo-light: #a9a9a9;
    --photo-dark: #3a3a3a;
  }
  * { margin: 0; padding: 0; box-sizing: border-box; }
  html, body { width: 1200px; height: 800px; overflow: hidden; }
  body {
    background: radial-gradient(ellipse at center, #ededed 0%, var(--backdrop) 70%, #bdbdbd 100%);
    font-family: "Tinos", serif;
  }
  .wine-label {
    position: absolute;
    left: 320px; top: 40px;
    width: 560px; height: 720px;
    background: radial-gradient(ellipse at 50% 40%, #262524 0%, var(--label-black) 60%, var(--label-edge) 100%);
    display: flex; flex-direction: column; align-items: center;
    padding-top: 30px;
  }
  .brand-crest { display: flex; flex-direction: column; align-items: center; width: 100%; }
  .crest-circle {
    width: 60px; height: 60px; border-radius: 50%;
    border: 3px solid var(--gold);
    position: relative; z-index: 1;
  }
  .scroll-ornament {
    width: 360px; height: 18px; margin-top: -12px;
    background: linear-gradient(90deg, transparent, var(--gold-deep) 20%, var(--gold) 50%, var(--gold-deep) 80%, transparent);
    opacity: 0.5; border-radius: 9px;
  }
  .brand-name {
    margin-top: 10px;
    font-family: "Cinzel", serif; font-weight: 400;
    color: var(--gold);
    font-size: 38px; letter-spacing: 4px; line-height: 1.05;
    text-align: center;
  }
  .brand-name span { display: block; font-size: 22px; letter-spacing: 8px; }
  .divider-ornament {
    width: 280px; height: 10px; margin-top: 10px;
    background: linear-gradient(90deg, transparent, var(--gold-deep) 30%, var(--gold) 50%, var(--gold-deep) 70%, transparent);
    opacity: 0.5; border-radius: 5px;
  }
  .dog-portrait {
    margin-top: 18px;
    width: 190px; height: 165px;
    background: radial-gradient(ellipse at 55% 55%, var(--photo-light) 0%, #6d6d6d 55%, var(--photo-dark) 100%);
  }
  .tagline {
    margin-top: 12px;
    font-family: "Cinzel", serif; color: var(--gold);
    font-size: 15px; letter-spacing: 1px;
  }
  .varietal {
    margin-top: 2px;
    font-family: "Cinzel", serif; font-weight: 400; color: var(--ivory);
    font-size: 42px; letter-spacing: 3px;
  }
  .small-ornament {
    width: 200px; height: 8px; margin-top: 4px;
    background: linear-gradient(90deg, transparent, var(--gold-deep) 40%, var(--gold) 50%, var(--gold-deep) 60%, transparent);
    opacity: 0.5; border-radius: 4px;
  }
  .contact { margin-top: 12px; text-align: center; color: var(--ivory); line-height: 1.4; font-style: normal; }
  .contact .place { font-size: 20px; letter-spacing: 1px; }
  .contact .web { font-size: 18px; }
  .contact .phone { font-size: 20px; }
  .origin-band {
    position: absolute; left: 0; right: 0; bottom: 30px;
    border-top: 3px solid var(--gold-band);
    padding-top: 10px; text-align: center;
  }
  .origin-band span {
    display: inline-block;
    background: linear-gradient(180deg, #d3bd8a, var(--gold-band));
    color: var(--label-black);
    font-size: 17px; padding: 4px 40px;
  }
</style>
</head>
<body>
  <main class="wine-label">
    <header class="brand-crest">
      <div class="crest-circle"></div>
      <div class="scroll-ornament" role="img" aria-label="Gold flourish scrollwork around the crest"></div>
      <h1 class="brand-name">Tavio<span>Berlanzi</span></h1>
      <div class="divider-ornament" role="img" aria-label="Gold scroll divider"></div>
    </header>
    <div class="dog-portrait" role="img" aria-label="Black and white photo of the dog wearing a flat cap"></div>
    <p class="tagline">Pup Baron's Pick</p>
    <h2 class="varietal">Pinot Noir</h2>
    <div class="small-ornament" role="img" aria-label="Small gold flourish"></div>
    <address class="contact">
      <div class="place">Sandmere Beach Florida</div>
      <div class="web">www.tavioberlanzi.example</div>
      <div class="phone">555-304-8812</div>
    </address>
    <footer class="origin-band"><span>Product de France</span></footer>
  </main>
</body>
</html>
```